Loft Plan Studio New Business Card

I am opening a new division of my business. I am a high end interior designer, and the new business is writing specs for construction projects. It will be marketed to the VERY high end contractor, architects and realtors. The client will actually be the one who pays us and signs the agreement, but it will be the contractor, architect or realtor that will recommend us. I have attached my current card and our previous logo which is still used on some of our paperwork. I would like the new logo to be connected in some way to what we are currently using. We will need to have room on the card for a person's name. I'd like to omit the address as we might be moving the office soon. The web address is www.LoftPlanStudio.example. For this design, please use my name, Marisol Whitfield.

Target Market(s)

High End Luxury Contractors, Realtors and Architects

Industry/Entity Type

Residential Construction

Contact Information for Business Card

Loft Plan Studio, Phone: 555-304-2917, www.LoftPlanStudio.example , Marisol Whitfield

Font styles to use
Sans Serif

Colors
ec1f27

Requirements
Must have
• Some visual reference to my current card and logos. Use the colors submitted on the business card I attached.
Nice to have
• A visual reference to my current card and logos. Use the colors submitted on the card I attached.
Should not have
• A physical address

```html
<!DOCTYPE html>
<html lang="en">
<head>
<meta charset="utf-8">
<title>Loft Plan Studio – Business Card</title>
<link href="https://fonts.googleapis.com/css2?family=Rokkitt:wght@400&family=Open+Sans:wght@400&display=swap" rel="stylesheet">
<style>
  :root {
    --bg: #e9e6e1;
    --card: #ffffff;
    --pattern: #ebebeb;
    --brand-red: #c8373a;
    --flourish: #e07a7c;
    --ink: #555557;
    --ink-soft: #6b6b6d;
  }
  * { margin: 0; padding: 0; box-sizing: border-box; }
  html, body {
    width: 1200px; height: 800px; overflow: hidden;
    background: var(--bg);
  }
  .card {
    position: absolute; left: 110px; top: 120px;
    width: 980px; height: 560px;
    background: var(--card);
    border-radius: 22px;
    box-shadow: 0 6px 24px rgba(0,0,0,0.12);
    overflow: hidden;
  }
  .card__pattern {
    position: absolute; left: 0; top: 0;
    width: 330px; height: 100%;
    background: var(--pattern);
  }
  .card__brand {
    position: absolute; left: 28px; top: 130px;
    width: 290px; height: 250px;
    display: flex; align-items: center; justify-content: center; gap: 12px;
  }
  .brand-mark {
    width: 16px; height: 16px;
    background: var(--brand-red);
    flex: none;
  }
  .brand-name {
    font-family: "Open Sans", sans-serif;
    font-weight: 400;
    font-size: 27px;
    line-height: 1;
    color: var(--ink);
    white-space: nowrap;
  }
  .card__details {
    position: absolute; left: 360px; right: 30px; top: 150px;
    text-align: center;
  }
  .flourish {
    display: block; margin: 0 auto 6px;
    width: 170px; height: 26px;
    background: var(--flourish);
    border-radius: 13px;
    opacity: 0.55;
  }
  .person-name {
    font-family: "Rokkitt", serif;
    font-weight: 400;
    font-size: 66px;
    line-height: 1;
    color: var(--ink);
  }
  .person-role {
    margin-top: 4px;
    font-family: "Open Sans", sans-serif;
    font-size: 15px;
    letter-spacing: 4.5px;
    color: var(--ink);
    text-transform: uppercase;
  }
  .contact {
    margin-top: 44px;
    font-family: "Open Sans", sans-serif;
    font-size: 29px;
    line-height: 1.35;
    color: var(--ink-soft);
  }
</style>
</head>
<body>
  <div class="card">
    <div class="card__pattern" role="img" aria-label="Embossed white triangle pattern"></div>
    <div class="card__brand">
      <span class="brand-mark"></span>
      <p class="brand-name">Loft Plan Studio</p>
    </div>
    <div class="card__details">
      <span class="flourish" role="img" aria-label="Red decorative flourish ornament"></span>
      <h1 class="person-name">Marisol Whitfield</h1>
      <p class="person-role">Commercial|Residential Design</p>
      <p class="contact">Phone: 555-304-2917<br>www.LoftPlanStudio.example</p>
    </div>
  </div>
</body>
</html>
```